Business Card Design

We recently had a new logo designed by Pixel Harbor. Now we want to create new business cards and letterhead that compliment our new logo.

We are audiologists in private practice specializing in hearing evaluations and fitting hearing aids. We want a clean and professional card.

We need business cards for each audiologist. The names and titles are:
Marlene Voss-Kettering, AuD
Audiologist

Jane Pratt, AuD
Audiologist

Corinna Lundt, AuD
Audiologist

We also need a business card with no provider. Just a generic one.

Finally, we need an appointment card. This is what the front desk uses to give to the patient with their next appointment date and time.

Target Market(s)

Our clients tend to be highly educated. They are older so the cards should be clean and easy to read. No squirrely font please.

Industry/Entity Type

Business

Contact Information for Business Card

27831 Birchmont Dr NE, suite 418
Seattle, WA 98177
206-555-0182

Requirements
Must have
• Clean
Easy to read
Professional
Modern but approachable / warm
Should not have
• Other pictures besides the logo

```html
<!DOCTYPE html>
<html lang="en">
<head>
<meta charset="utf-8">
<title>Alderbrook Hearing Services – Business Cards</title>
<link rel="stylesheet" href="https://fonts.googleapis.com/css2?family=Carlito:wght@400;700&display=swap">
<style>
  :root {
    --stage-light: #5a5a5a;
    --stage-dark: #121212;
    --card-bg: #ffffff;
    --navy: #173c5e;
    --text-grey: #5f6368;
    --icon-blue: #1f6a98;
    --rule-teal: #5cc0aa;
    --teal-edge: #5eb7a1;
    --teal-mid: #b6dbd3;
    --teal-end: #35aa94;
    --blue-edge: #1c4674;
    --blue-mid: #2c5fae;
    --blue-end: #1d4a78;
    --brand-dot: #4a8fa8;
  }
  * { margin: 0; padding: 0; box-sizing: border-box; }
  html, body { width: 1000px; height: 1200px; overflow: hidden; }
  body {
    background: radial-gradient(ellipse at 50% 50%, var(--stage-light) 0%, #3a3a3a 45%, var(--stage-dark) 100%);
    font-family: "Carlito", "Calibri", sans-serif;
    position: relative;
  }
  .card {
    position: absolute;
    left: 163px;
    width: 676px;
    height: 396px;
    background: var(--card-bg);
    overflow: hidden;
    box-shadow: 0 14px 22px rgba(0,0,0,0.55);
  }
  .card--teal { top: 153px; }
  .card--navy { top: 641px; }
  .card__wave { position: absolute; left: 0; top: 0; width: 676px; height: 396px; }
  .brand {
    position: absolute;
    left: 77px;
    top: 62px;
    display: flex;
    align-items: center;
    gap: 10px;
  }
  .brand__dot {
    width: 52px; height: 52px; border-radius: 50%;
    background: var(--brand-dot);
  }
  .brand__name {
    font-weight: 700;
    font-size: 19px;
    color: var(--navy);
    letter-spacing: 0.3px;
  }
  .person__name {
    position: absolute;
    right: 54px;
    top: 171px;
    font-size: 25px;
    font-weight: 700;
    color: var(--navy);
  }
  .person__rule {
    position: absolute;
    left: 97px;
    top: 216px;
    width: 386px;
    height: 2px;
    background: var(--rule-teal);
  }
  .person__title {
    position: absolute;
    right: 54px;
    top: 206px;
    font-size: 15px;
    color: var(--text-grey);
  }
  .contact {
    position: absolute;
    right: 50px;
    top: 274px;
    list-style: none;
    text-align: right;
    font-size: 15px;
    color: var(--text-grey);
    line-height: 21px;
  }
  .contact__item { display: flex; justify-content: flex-end; align-items: center; gap: 7px; }
  .contact__icon { width: 14px; height: 14px; fill: var(--icon-blue); }
</style>
</head>
<body>

<section class="card card--teal">
  <svg class="card__wave" viewBox="0 0 676 396" aria-hidden="true">
    <defs>
      <linearGradient id="tealWave" x1="0" x2="1" y1="0" y2="0">
        <stop offset="0" stop-color="var(--teal-edge)"/>
        <stop offset="0.4" stop-color="var(--teal-mid)"/>
        <stop offset="1" stop-color="var(--teal-end)"/>
      </linearGradient>
    </defs>
    <path d="M0 257 Q 330 385 676 364 L676 396 L0 396 Z" fill="url(#tealWave)"/>
  </svg>
  <div class="brand"><span class="brand__dot"></span><span class="brand__name">Alderbrook Hearing Services</span></div>
  <h1 class="person__name">Marlene Voss-Kettering</h1>
  <div class="person__rule"></div>
  <p class="person__title">AuD, Audiologist</p>
  <ul class="contact">
    <li class="contact__item">27831 Birchmont Dr NE, suite 418 Seattle, WA 98177
      <svg class="contact__icon" viewBox="0 0 16 16"><path d="M8 1 L0.5 8 H3 V15 H6.5 V10.5 H9.5 V15 H13 V8 H15.5 Z"/></svg></li>
    <li class="contact__item">206-555-0182
      <svg class="contact__icon" viewBox="0 0 16 16"><path d="M3.6 1 L6 4.2 L4.6 6 Q6 9.5 10 11.4 L11.8 10 L15 12.4 L13.3 15 Q6.5 14.6 1 3 Z"/></svg></li>
  </ul>
</section>

<section class="card card--navy">
  <svg class="card__wave" viewBox="0 0 676 396" aria-hidden="true">
    <defs>
      <linearGradient id="navyWave" x1="0" x2="1" y1="0" y2="0">
        <stop offset="0" stop-color="var(--blue-edge)"/>
        <stop offset="0.55" stop-color="var(--blue-mid)"/>
        <stop offset="1" stop-color="var(--blue-end)"/>
      </linearGradient>
    </defs>
    <path d="M0 257 Q 330 385 676 364 L676 396 L0 396 Z" fill="url(#navyWave)"/>
  </svg>
  <div class="brand"><span class="brand__dot"></span><span class="brand__name">Alderbrook Hearing Services</span></div>
  <h2 class="person__name">Marlene Voss-Kettering</h2>
  <div class="person__rule"></div>
  <p class="person__title">AuD, Audiologist</p>
  <ul class="contact">
    <li class="contact__item">27831 Birchmont Dr NE, suite 418 Seattle, WA 98177
      <svg class="contact__icon" viewBox="0 0 16 16"><path d="M8 1 L0.5 8 H3 V15 H6.5 V10.5 H9.5 V15 H13 V8 H15.5 Z"/></svg></li>
    <li class="contact__item">206-555-0182
      <svg class="contact__icon" viewBox="0 0 16 16"><path d="M3.6 1 L6 4.2 L4.6 6 Q6 9.5 10 11.4 L11.8 10 L15 12.4 L13.3 15 Q6.5 14.6 1 3 Z"/></svg></li>
  </ul>
</section>

</body>
</html>
```